Hi there,
I'm looking for a dynamic business card design to compliment my car detailing business ([url removed, login to view] [url removed, login to view]).

I'll leave the designing to you people, but I do require the following information to be on the card:
Polished Horizon,
Tom Bexley,
Detailing & Valeting Specialist,
Over 10 Years Experience.
Could the website ([url removed, login to view]) be put on the card please.

Contact Information can be got from the website or here: 07618 275093 Email: tom@[url removed, login to view] and I also require the company logo to be on the card too.

Many thanks.

Tom.

```html
<!DOCTYPE html>
<html lang="en">
<head>
<meta charset="utf-8">
<title>Polished Horizon – Business Card</title>
<link rel="stylesheet" href="https://fonts.googleapis.com/css2?family=Tinos&family=Mulish:wght@400;500&display=swap">
<style>
  :root {
    --page: #ffffff;
    --leather-light: #2c2c2c;
    --leather-mid: #1c1c1c;
    --leather-dark: #0f0f0f;
    --silver: #d9d9d9;
    --white: #f4f4f4;
    --band-light: #f2f2f2;
    --band-mid: #c9c9c9;
    --band-dark: #9a9a9a;
    --ink: #2a2a2a;
  }
  * { margin: 0; padding: 0; box-sizing: border-box; }
  html, body {
    width: 857px; height: 1200px; overflow: hidden;
    background: var(--page);
  }
  .sheet { position: relative; width: 857px; height: 1200px; }
  .card {
    position: absolute;
    width: 797px;
    overflow: hidden;
    box-shadow: 4px 6px 10px rgba(0,0,0,0.35);
    color: var(--white);
    text-align: center;
  }
  .card-front { left: 38px; top: 26px; height: 454px; }
  .card-back  { left: 29px; top: 603px; height: 451px; }
  .leather {
    position: absolute; inset: 0;
    background: radial-gradient(ellipse at 50% 40%, var(--leather-light) 0%, var(--leather-mid) 55%, var(--leather-dark) 100%);
  }
  .content { position: absolute; left: 0; right: 0; }
  .brand-name {
    top: 200px;
    font-family: "Tinos", serif;
    font-size: 64px;
    line-height: 1.1;
    letter-spacing: 3px;
    text-transform: uppercase;
    color: var(--silver);
  }
  .front-web {
    top: 360px;
    font-family: "Mulish", sans-serif;
    font-size: 27px;
    font-weight: 500;
    color: var(--white);
  }
  .person-name {
    top: 86px;
    font-family: "Tinos", serif;
    font-size: 56px;
    color: var(--white);
  }
  .experience {
    top: 150px;
    font-family: "Tinos", serif;
    font-size: 23px;
    color: var(--white);
  }
  .role-band {
    top: 221px; height: 59px;
    background: linear-gradient(to right, var(--band-dark) 0%, var(--band-light) 30%, var(--band-mid) 60%, var(--band-light) 80%, var(--band-dark) 100%);
    font-family: "Mulish", sans-serif;
    font-size: 31px;
    line-height: 59px;
    color: var(--ink);
  }
  .back-web {
    top: 318px;
    font-family: "Mulish", sans-serif;
    font-size: 26px;
    font-weight: 500;
  }
  .contact {
    top: 356px;
    font-family: "Tinos", serif;
    font-size: 22px;
    line-height: 30px;
    color: var(--silver);
  }
</style>
</head>
<body>
<main class="sheet">
  <section class="card card-front">
    <div class="leather" role="img" aria-label="Black leather texture background"></div>
    <h1 class="content brand-name">Polished<br>Horizon</h1>
    <p class="content front-web">www.polishedhorizon.co.uk</p>
  </section>

  <section class="card card-back">
    <div class="leather" role="img" aria-label="Black leather texture background"></div>
    <h2 class="content person-name">Tom Bexley</h2>
    <p class="content experience">Over 10 Years Experience</p>
    <p class="content role-band">Detailing &amp; Valeting Specialist</p>
    <p class="content back-web">www.polishedhorizon.co.uk</p>
    <p class="content contact">Email: tom@polishedhorizon.co.uk<br>Phone : 07618 275093</p>
  </section>
</main>
</body>
</html>
```